Welding company needs a business card

We are looking for a logo and business card.

Contact Information for Business Card

418 Cobblestone Lane
York, PA 17402
410-555-0173
Rmfabworksco@quorvamail.com

```html
<!DOCTYPE html>
<html lang="en">
<head>
<meta charset="UTF-8">
<title>Rmfab Works – Business Card</title>
<link href="https://fonts.googleapis.com/css2?family=Lato:wght@400;700;900&display=swap" rel="stylesheet">
<style>
  :root {
    --orange: #ef5323;
    --blue: #2f72b4;
    --ink: #2a2a2a;
    --paper: #ffffff;
    --stage: #e9edf1;
    --art-blue: #eef2f9;
    --art-peach: #fcefe6;
  }
  * { margin: 0; padding: 0; box-sizing: border-box; }
  html, body {
    width: 1200px; height: 800px; overflow: hidden;
    background: var(--stage);
    font-family: "Lato", Arial, sans-serif;
  }
  .card {
    position: absolute; left: 75px; top: 100px;
    width: 1050px; height: 600px;
    background: linear-gradient(135deg, var(--orange) 0%, var(--blue) 28%, var(--orange) 50%, var(--blue) 75%, var(--orange) 100%);
    box-shadow: 0 10px 30px rgba(0,0,0,.18);
  }
  .card-face {
    position: absolute; inset: 28px;
    background: var(--paper);
    overflow: hidden;
  }
  .brand {
    position: absolute; left: 50px; top: 92px;
    display: flex; align-items: center; gap: 16px;
  }
  .brand-dot {
    width: 34px; height: 34px; border-radius: 50%;
    background: var(--orange);
  }
  .brand-name {
    font-weight: 900; font-size: 66px; color: var(--ink);
    letter-spacing: .5px;
  }
  .decor-art {
    position: absolute; left: 0; top: 300px;
    width: 470px; height: 244px;
    background: linear-gradient(90deg, var(--art-blue) 0%, var(--art-blue) 50%, var(--art-peach) 100%);
  }
  .contact {
    position: absolute; left: 540px; top: 215px;
    color: var(--ink);
  }
  .contact-name {
    font-weight: 700; font-size: 40px; color: var(--blue);
  }
  .contact-role {
    font-size: 24px; color: var(--orange); margin-top: 2px;
  }
  .contact-lines { margin-top: 26px; }
  .contact-line {
    display: flex; align-items: center; gap: 18px;
    font-size: 26px; margin-bottom: 10px;
  }
  .contact-line svg { width: 30px; height: 26px; flex: none; }
  .address {
    margin-top: 28px; font-size: 27px; line-height: 1.3;
  }
</style>
</head>
<body>
  <div class="card">
    <div class="card-face">
      <div class="decor-art" role="img" aria-label="Faint background illustration of a welding torch with flame"></div>

      <div class="brand">
        <span class="brand-dot"></span>
        <span class="brand-name">Rmfab Works</span>
      </div>

      <div class="contact">
        <div class="contact-name">Darren Kale Voss</div>
        <div class="contact-role">Founder</div>

        <div class="contact-lines">
          <div class="contact-line">
            <svg viewBox="0 0 30 26" aria-hidden="true">
              <path d="M2 9 Q15 0 28 9 L25 12 L20 10 L20 7 Q15 5 10 7 L10 10 L5 12 Z" fill="var(--orange)"/>
              <path d="M8 12 L22 12 L26 24 L4 24 Z" fill="var(--orange)"/>
              <circle cx="15" cy="18" r="3.5" fill="#fff"/>
            </svg>
            <span>410-555-0173</span>
          </div>
          <div class="contact-line">
            <svg viewBox="0 0 30 26" aria-hidden="true">
              <rect x="1" y="4" width="28" height="19" fill="var(--orange)"/>
              <path d="M1 4 L15 15 L29 4" fill="none" stroke="#fff" stroke-width="2"/>
            </svg>
            <span>Rmfabworksco@quorvamail.com</span>
          </div>
        </div>

        <div class="address">
          418 Cobblestone Lane<br>
          York, PA 17402
        </div>
      </div>
    </div>
  </div>
</body>
</html>
```